Business card design needed

www.marlonfab.com.au
Our primary services:
On-site welding.
On-site industrial maintenance.
On-site repairs and capital works projects specialising in pipe fabrication.
Our ability to work on-site with our dedicated mobile equipment is essential to our capability to provide a quality maintenance service to our customers. We are capable of providing a full team of qualified boilermakers that can work either to your plan or project manage if a plan has not been developed.
Industry/Entity Type
Industrial
Contact Information for Business Card
company name- MARLON FAB PTY LTD
story - industrial steel fabrication, constructions and pipelines
Director - Greg Hadley
workshop address - shed 7, 3862 kemble rd Tully
postal address - P.O BOX 628 TULLY Q 4854
mobile - 0429385106
w/shop phone - 0752937048
fax - 0752938159
email - admin@marlonfab.com.au
web - www.marlonfab.com.au
Logo Text
MARLON FAB pty ltd
Look and feel

```html
<!DOCTYPE html>
<html lang="en">
<head>
<meta charset="utf-8">
<title>Marlon Fab business card</title>
<link rel="stylesheet" href="https://fonts.googleapis.com/css2?family=Arimo:wght@400;500&family=Tinos:wght@400;700&display=swap">
<style>
  :root {
    --backdrop: #e9e7e4;
    --card-white: #ffffff;
    --brand-violet: #5a58a5;
    --brand-violet-dark: #3f3d8c;
    --ink: #1f1f24;
    --ink-soft: #55555f;
    --on-violet: #ffffff;
  }
  * { margin: 0; padding: 0; box-sizing: border-box; }
  html, body { width: 1200px; height: 873px; overflow: hidden; }
  body {
    background: var(--backdrop);
    display: flex;
    align-items: center;
    justify-content: center;
    gap: 60px;
  }
  .card {
    width: 500px;
    height: 286px;
    position: relative;
    box-shadow: 0 10px 28px rgba(0,0,0,0.18);
  }

  /* Front */
  .card--front { background: var(--card-white); color: var(--ink); }
  .front__brand {
    position: absolute;
    top: 34px;
    right: 36px;
    display: flex;
    align-items: center;
    gap: 10px;
  }
  .brand__square {
    width: 16px; height: 16px;
    background: var(--brand-violet-dark);
  }
  .brand__name {
    font-family: "Arimo", sans-serif;
    font-weight: 500;
    font-size: 30px;
    letter-spacing: 1px;
    line-height: 1;
    color: var(--brand-violet-dark);
  }
  .front__tagline {
    position: absolute;
    top: 84px;
    left: 36px;
    right: 36px;
    text-align: right;
    font-family: "Tinos", serif;
    font-size: 12px;
    letter-spacing: 1.3px;
    color: var(--brand-violet);
  }
  .front__person {
    position: absolute;
    top: 132px;
    left: 0; right: 0;
    text-align: center;
    font-family: "Tinos", serif;
  }
  .person__name { font-weight: 700; font-size: 16px; letter-spacing: 0.5px; }
  .person__role { font-size: 11px; color: var(--ink-soft); margin-top: 2px; }
  .front__contacts {
    position: absolute;
    left: 36px;
    bottom: 28px;
    font-family: "Tinos", serif;
    font-size: 11.5px;
    line-height: 1.7;
    list-style: none;
  }
  .contact__label {
    font-size: 7.5px;
    font-weight: 700;
    letter-spacing: 0.6px;
    color: var(--brand-violet);
    margin-right: 3px;
    text-transform: uppercase;
  }
  .contact__sep { margin: 0 5px; }

  /* Back */
  .card--back { background: var(--brand-violet); color: var(--on-violet); }
  .back__services {
    position: absolute;
    top: 38px;
    left: 0; right: 0;
    text-align: center;
    font-family: "Arimo", sans-serif;
    font-size: 14px;
    line-height: 1.55;
    list-style: none;
  }
  .back__brand {
    position: absolute;
    left: 60px;
    bottom: 58px;
    display: flex;
    align-items: center;
    gap: 10px;
  }
  .back__brand .brand__square { background: var(--on-violet); }
  .back__brand .brand__name { color: var(--on-violet); }
</style>
</head>
<body>
  <section class="card card--front" aria-label="Business card front">
    <div class="front__brand">
      <span class="brand__square"></span>
      <span class="brand__name">MARLON FAB</span>
    </div>
    <p class="front__tagline">INDUSTRIAL STEEL FABRICATION • CONSTRUCTIONS • PIPELINES</p>
    <div class="front__person">
      <p class="person__name">GREG HADLEY</p>
      <p class="person__role">Director</p>
    </div>
    <ul class="front__contacts">
      <li><span class="contact__label">Mobile</span>0429 385 106<span class="contact__sep">•</span><span class="contact__label">Email</span>admin@marlonfab.com.au<span class="contact__sep">•</span></li>
      <li><span class="contact__label">Tel</span>0752 937 048<span class="contact__sep">•</span><span class="contact__label">Fax</span>0752 938 159<span class="contact__sep">•</span>www.marlonfab.com.au<span class="contact__sep">•</span></li>
      <li><span class="contact__label">Workshop</span>Shed 7, 3862 Kemble Rd Tully<span class="contact__sep">•</span></li>
    </ul>
  </section>

  <section class="card card--back" aria-label="Business card back">
    <ul class="back__services">
      <li>On-site welding</li>
      <li>On-site industrial maintenance</li>
      <li>On-site repairs and capital works projects</li>
      <li>specialising in pipe fabrication</li>
    </ul>
    <div class="back__brand">
      <span class="brand__square"></span>
      <span class="brand__name">MARLON FAB</span>
    </div>
  </section>
</body>
</html>
```